Premium Personal Brand — Facebook Banner (Used Across All Platforms)

Update — Additional Color Direction
In addition to the dark charcoal/slate direction already described, I'm also interested in seeing variants with:
Dark navy blue — Deep, authoritative, intelligence-community feel. Same textured/matte treatment, not flat or bright.
Warm charcoal with steel blue accent — Keep the dark base but introduce a subtle steel blue gradient, accent line, or tonal shift. Sophisticated, modern, adds dimension without adding color noise.
Both should maintain the same premium, restrained, architectural feel described in the original brief. No bright blues, no corporate PowerPoint energy — think midnight, think depth, think weight.
Everything else in the brief remains the same.
I am building a premium personal brand as an executive advisor to founders ($5M+ revenue).
This contest is Facebook-banner–focused, but the design must represent a visual system that will be reused across:
- LinkedIn
- YouTube
I- nstagram
- X (Twitter)
- Website hero sections and other brand touchpoints
Think of the Facebook banner as the primary expression of the brand — not a one-off graphic.
This project is about discovering a high-end visual style and brand feel, not decoration.
What to design
Please submit one cohesive visual system, shown primarily as:
- Facebook banner (primary focus)
The same design language should clearly translate to all platforms listed above.
Designers are responsible for using the current recommended dimensions for each platform.
Quick clarification on background direction:
Backgrounds should have depth and texture, not flat color fields. Avoid pure white, light grey, or solid black backgrounds. Think matte, architectural materials — stone, graphite, concrete, steel — not blank canvases. Subtle tonal variation is encouraged. Obvious gradients or decorative patterns are not.
Text to use
Primary Headline:
- Your Business Is Too Valuable To Be Run On Hope.
Subheadline:
- You didn’t build a business to become its prisoner.
Name:
Paul Whitaker
The headline should be the dominant visual element.
Logo note (important)
My personal logo is currently being finalized.
For this contest:
- Use a simple “PW” monogram placeholder
- Clean, bold, geometric sans-serif
- Do not design a logo
- The winning design must allow an easy logo swap later.
Headshot note (important)
- Please do not include a headshot in the banner design.
- Most platforms display a circular profile image separately.
- The banner should stand on its own using typography, layout, and tone only.
- Design the banner assuming the profile photo will sit nearby, not inside the banner.
Style direction
The design should feel:
- Premium
- Calm
- Confident
- Restrained
- High-trust
- Dark, neutral backgrounds are preferred.
- Fewer elements are better than more.
Think:
- Owner-level advisor
- Private equity / boardroom tone
- Industrial, Modern, Minimalist, Elite, Architectural, not decorative
What to avoid
Please do not submit designs that feel:
- Promotional, hype-driven, or salesy
- Like a coach, guru, or agency
- Bright, colorful, or gradient-heavy
- Busy or over-designed
- Based on stock photos
- No motivational speaker energy.
Reaction test
- If someone sees this banner on Facebook (or later on LinkedIn, YouTube, etc.), the reaction should be:
“That person is serious. I’d trust them with important decisions.”
Final note
- I am not looking for many variations.
- I am looking for one strong visual direction you believe in.
Simple beats clever.
- Restraint beats decoration.

```html
<!DOCTYPE html>
<html lang="en">
<head>
<meta charset="utf-8">
<title>Paul Whitaker — Banner</title>
<link href="https://fonts.googleapis.com/css2?family=Montserrat:wght@300;400;700&display=swap" rel="stylesheet">
<style>
  :root {
    --page: #ffffff;
    --graphite-dark: #1f2226;
    --graphite-mid: #2b2f34;
    --graphite-light: #363a40;
    --text-primary: #ffffff;
    --text-secondary: #eef0f2;
    --text-muted: #d9dcdf;
  }
  * { margin: 0; padding: 0; box-sizing: border-box; }
  html, body {
    width: 1200px;
    height: 600px;
    overflow: hidden;
    background: var(--page);
    font-family: "Montserrat", sans-serif;
  }
  .canvas {
    position: relative;
    width: 1200px;
    height: 600px;
    background: var(--page);
  }
  .banner {
    position: absolute;
    left: 60px;
    top: 60px;
    width: 1080px;
    height: 480px;
    overflow: hidden;
  }
  .banner-texture {
    position: absolute;
    inset: 0;
    background:
      radial-gradient(ellipse 60% 55% at 72% 35%, rgba(70, 75, 82, 0.35), transparent 70%),
      radial-gradient(ellipse 50% 50% at 45% 80%, rgba(60, 64, 70, 0.30), transparent 70%),
      radial-gradient(ellipse 45% 60% at 5% 50%, rgba(15, 17, 20, 0.45), transparent 70%),
      linear-gradient(135deg, var(--graphite-dark) 0%, var(--graphite-mid) 45%, var(--graphite-light) 70%, var(--graphite-mid) 100%);
  }
  .headline {
    position: absolute;
    left: 0;
    right: 0;
    top: 201px;
    text-align: center;
    font-weight: 700;
    font-size: 29px;
    line-height: 1;
    letter-spacing: 0.3px;
    color: var(--text-primary);
  }
  .subheadline {
    position: absolute;
    left: 0;
    right: 0;
    top: 258px;
    text-align: center;
    font-weight: 400;
    font-size: 18.6px;
    line-height: 1;
    letter-spacing: 1.4px;
    color: var(--text-secondary);
  }
  .signature {
    position: absolute;
    left: 0;
    right: 0;
    top: 401px;
    display: flex;
    justify-content: center;
    align-items: baseline;
    gap: 13px;
  }
  .monogram {
    font-weight: 700;
    font-size: 27px;
    letter-spacing: -1px;
    color: var(--text-primary);
    line-height: 1;
  }
  .name {
    font-weight: 300;
    font-size: 20px;
    letter-spacing: 0.4px;
    color: var(--text-muted);
    line-height: 1;
  }
</style>
</head>
<body>
  <div class="canvas">
    <section class="banner">
      <div class="banner-texture" role="img" aria-label="Dark graphite woven-texture background"></div>
      <h1 class="headline">Your Business Is Too Valuable To Be Run On Hope.</h1>
      <p class="subheadline">You didn’t build a business to become its prisoner.</p>
      <div class="signature">
        <span class="monogram">PW</span>
        <span class="name">Paul Whitaker</span>
      </div>
    </section>
  </div>
</body>
</html>
```